Bright Rivers Exhibition Banner (stand)

We are looking for a standing banner design, to stand outside our workshop rooms, or at trade shows.

Please see designs from recent contests to give you direction.
However in this one we would like to see the introduction of color in the form of an image.

It should inform people about us and our workshops.

Text could include:

Transform your team
Strengthening Collaboration
Unlock human potential

Keywords might be: Trust, creativity, collaboration, connection

-> Team building workshop today.

Or you could come up with something of your own.

It should be tall: W:85 cm H:206 cm

Industry/Entity Type

Various Corproate

Requirements
Must have
• It should be vertical: H:206 cm W:85 cm

```html
<!DOCTYPE html>
<html lang="en">
<head>
<meta charset="utf-8">
<title>Bright Rivers – Exhibition Banner</title>
<link rel="stylesheet" href="https://fonts.googleapis.com/css2?family=Montserrat:wght@500&family=Poppins:wght@600&family=Saira:wght@400;500;700;800;900&display=swap">
<style>
  :root {
    --page-bg: #4f4f4f;
    --banner-top: #e6e6e4;
    --banner-bottom: #d6d7d6;
    --ink-dark: #2b3a3c;
    --ink-slate: #4b5e62;
    --ink-muted: #7f9396;
    --band-mid: #5f7174;
    --white: #ffffff;
    --forest-dark: #2f3c44;
    --forest-mid: #5f6e78;
  }
  * { box-sizing: border-box; margin: 0; padding: 0; }
  html, body {
    width: 1103px; height: 1200px; overflow: hidden;
    background: var(--page-bg);
  }
  .banner {
    position: absolute; left: 316px; top: 30px;
    width: 470px; height: 1140px; overflow: hidden;
    background: linear-gradient(180deg, var(--banner-top), var(--banner-bottom));
    font-family: "Saira", sans-serif;
    text-align: center;
  }
  .brand-dot {
    position: absolute; left: 50%; top: 78px;
    width: 64px; height: 64px; margin-left: -32px;
    border-radius: 50%; background: var(--ink-muted);
  }
  .brand-name {
    position: absolute; left: 0; right: 0; top: 166px;
    font-family: "Montserrat", sans-serif; font-weight: 500;
    font-size: 31px; letter-spacing: 2px; color: var(--ink-dark);
  }
  .brand-tagline {
    position: absolute; left: 0; right: 0; top: 208px;
    font-family: "Montserrat", sans-serif; font-weight: 500;
    font-size: 9px; line-height: 12px; letter-spacing: 1.6px; color: var(--ink-muted);
  }
  .headline-lead {
    position: absolute; left: 0; right: 0; top: 268px;
    font-size: 37px; font-weight: 500; line-height: 44px; color: var(--ink-slate);
  }
  .headline-main {
    position: absolute; left: 0; right: 0; top: 306px;
    font-size: 58px; font-weight: 900; line-height: 66px; letter-spacing: 0.5px;
    color: var(--ink-dark);
  }
  .band {
    position: absolute; height: 26px;
    color: var(--white); font-size: 19px; line-height: 26px;
    letter-spacing: 0.6px; white-space: nowrap;
  }
  .band b { font-weight: 800; }
  .band span { font-weight: 400; }
  .band-collab { left: 29px; width: 412px; top: 374px; background: var(--band-mid); }
  .band-potential { left: 65px; width: 340px; top: 404px; background: var(--ink-dark); }

  .values {
    position: absolute; left: 125px; top: 466px; width: 219px; height: 215px;
  }
  .values-art {
    position: absolute; left: 32px; top: 30px; width: 158px; height: 158px;
    background: linear-gradient(135deg, var(--ink-muted), var(--ink-slate) 55%, var(--ink-dark));
  }
  .value {
    position: absolute; font-weight: 700; line-height: 1;
    white-space: nowrap; text-align: left;
  }
  .value-trust {
    left: 93px; top: 0; font-size: 22px; letter-spacing: 9px; color: var(--ink-slate);
  }
  .value-collab {
    left: 4px; top: 2px; font-size: 12px; letter-spacing: 2.5px; color: var(--ink-dark);
    writing-mode: vertical-rl;
  }
  .value-connection {
    left: 201px; top: 80px; font-size: 13px; letter-spacing: 4.5px; color: var(--ink-muted);
    writing-mode: vertical-rl; transform: rotate(180deg);
  }
  .value-creativity {
    left: 0; top: 199px; font-size: 14.5px; letter-spacing: 4px; color: var(--ink-slate);
  }

  .cta {
    position: absolute; left: 133px; top: 712px; width: 202px; height: 38px;
    border-radius: 19px; background: var(--ink-dark); color: var(--white);
    font-family: "Poppins", sans-serif; font-weight: 600; font-size: 24px; line-height: 40px;
  }
  .cta-note {
    position: absolute; left: 0; right: 0; top: 755px;
    font-size: 20px; font-weight: 800; letter-spacing: 0.6px; color: var(--ink-slate);
  }
  .forest {
    position: absolute; left: 0; right: 0; top: 740px; bottom: 0;
    background: linear-gradient(180deg,
      rgba(214,215,214,0) 0%,
      rgba(190,195,198,0.6) 22%,
      var(--forest-mid) 50%,
      var(--forest-dark) 100%);
  }
  .banner > *:not(.forest) { z-index: 1; }
</style>
</head>
<body>
  <main class="banner">
    <div class="forest" role="img" aria-label="Photograph of a misty evergreen forest seen from above"></div>

    <div class="brand-dot"></div>
    <div class="brand-name">BRIGHT RIVERS</div>
    <div class="brand-tagline">FACILITATING GROWTH<br>UNLOCKING HUMAN POTENTIAL</div>

    <h1 class="headline-lead">Transform</h1>
    <h2 class="headline-main">YOUR TEAM</h2>

    <div class="band band-collab"><b>STRENGTHENING</b> <span>COLLABORATION</span></div>
    <div class="band band-potential"><span>UNLOCK</span> <b>HUMAN POTENTIAL</b></div>

    <div class="values">
      <div class="values-art" role="img" aria-label="Illustration of four hands clasping each other's wrists in a square"></div>
      <div class="value value-trust">TRUST</div>
      <div class="value value-collab">COLLABORATION</div>
      <div class="value value-connection">CONNECTION</div>
      <div class="value value-creativity">CREATIVITY</div>
    </div>

    <div class="cta">Join Today</div>
    <div class="cta-note">TEAM BUILDING WORKSHOP</div>
  </main>
</body>
</html>
```